Business Card Design

Hoping for a black background business card, minimalistic design.
With the Marble Crest logo you created in white.

I would like to include:
My Name and title
Address (street address)
Reception: (phone number)
Fax: (fax number)
Reception: (email address)
Direct email: (email address)
Instagram: (ig handle)

```html
<!DOCTYPE html>
<html lang="en">
<head>
<meta charset="utf-8">
<title>Marble Crest — Business Card</title>
<link rel="stylesheet" href="https://fonts.googleapis.com/css2?family=Open+Sans:wght@400;600;700&display=swap">
<style>
  :root {
    --backdrop: #2b2b2e;
    --card: #1f1f22;
    --ink: #ffffff;
    --ink-soft: #d9d9dc;
    --rule: #8a8a90;
  }
  * { box-sizing: border-box; margin: 0; padding: 0; }
  html, body {
    width: 1200px; height: 780px; overflow: hidden;
    background: var(--backdrop);
    font-family: "Open Sans", Arial, sans-serif;
    color: var(--ink);
  }
  .sheet {
    position: relative; width: 1200px; height: 780px;
    display: flex; align-items: center; justify-content: center; gap: 40px;
  }
  .card {
    position: relative; width: 540px; height: 310px;
    background: var(--card); border-radius: 4px;
    box-shadow: 0 10px 30px rgba(0,0,0,.45);
    overflow: hidden;
  }
  .card-art { position: absolute; inset: 0; }

  /* front */
  .brand-mark { position: absolute; left: 50px; top: 40px; width: 150px; text-align: center; }
  .brand-mark .brand-name {
    margin-top: 10px; font-size: 14px; font-weight: 600;
    letter-spacing: 3px; text-transform: uppercase; color: var(--ink);
  }
  .person { position: absolute; left: 300px; top: 44px; }
  .person-name { font-size: 26px; font-weight: 700; line-height: 1.1; }
  .person-title { font-size: 13px; color: var(--ink-soft); margin-bottom: 12px; }
  .contact-list { list-style: none; }
  .contact-list li {
    display: flex; align-items: center; gap: 8px;
    font-size: 13px; line-height: 1.7; white-space: nowrap;
  }
  .contact-list .note { font-size: 10px; color: var(--ink-soft); }
  .contact-list svg { width: 13px; height: 13px; flex: none; }
  .address {
    position: absolute; left: 40px; bottom: 22px;
    font-size: 13px; color: var(--ink-soft); letter-spacing: .3px;
  }

  /* back */
  .wordmark {
    position: absolute; left: 225px; top: 136px;
    font-size: 30px; font-weight: 600; letter-spacing: 6px;
    text-transform: uppercase; color: var(--ink);
  }
</style>
</head>
<body>
<main class="sheet">

  <section class="card card-front" aria-label="Business card front">
    <svg class="card-art" viewBox="0 0 540 310" aria-hidden="true">
      <line x1="276" y1="36" x2="214" y2="222" stroke="var(--rule)" stroke-width="1"/>
    </svg>
    <div class="brand-mark">
      <svg width="150" height="150" viewBox="0 0 150 150" aria-hidden="true">
        <circle cx="75" cy="75" r="68" fill="none" stroke="var(--ink)" stroke-width="8"/>
      </svg>
      <div class="brand-name">Marble Crest</div>
    </div>

    <div class="person">
      <h1 class="person-name">Lena Varga</h1>
      <p class="person-title">Co-Founder</p>
      <ul class="contact-list">
        <li>
          <svg viewBox="0 0 16 16" aria-hidden="true"><path d="M3 1.5l3 3-1.5 2c1 2 2.5 3.5 4.5 4.5l2-1.5 3 3-2 2C6 14 2 10 1.5 3.5z" fill="var(--ink)"/></svg>
          (555) 014-2290
        </li>
        <li>
          <svg viewBox="0 0 16 16" aria-hidden="true"><rect x="4" y="1.5" width="8" height="4" fill="none" stroke="var(--ink)" stroke-width="1.4"/><rect x="1.5" y="5.5" width="13" height="6" rx="1" fill="var(--ink)"/><rect x="4" y="10" width="8" height="4.5" fill="var(--ink)" stroke="var(--card)" stroke-width="1"/></svg>
          (555) 014-7731
        </li>
        <li>
          <svg viewBox="0 0 16 16" aria-hidden="true"><circle cx="8" cy="8" r="6" fill="none" stroke="var(--ink)" stroke-width="1.6"/></svg>
          @marblecrest.studio
        </li>
        <li>
          <svg viewBox="0 0 16 16" aria-hidden="true"><rect x="1.5" y="3.5" width="13" height="9" fill="none" stroke="var(--ink)" stroke-width="1.4"/><path d="M1.5 3.5L8 9l6.5-5.5" fill="none" stroke="var(--ink)" stroke-width="1.4"/></svg>
          hello@marblecrest.co <span class="note">(Reception)</span>
        </li>
        <li>
          <svg viewBox="0 0 16 16" aria-hidden="true"><rect x="1.5" y="3.5" width="13" height="9" fill="none" stroke="var(--ink)" stroke-width="1.4"/><path d="M1.5 3.5L8 9l6.5-5.5" fill="none" stroke="var(--ink)" stroke-width="1.4"/></svg>
          lena@marblecrest.co <span class="note">(Direct email)</span>
        </li>
      </ul>
    </div>

    <p class="address">1840 Linden Ave. Suite 310 Millbrook, TX 75014</p>
  </section>

  <section class="card card-back" aria-label="Business card back">
    <svg class="card-art" viewBox="0 0 540 310" aria-hidden="true">
      <circle cx="140" cy="150" r="44" fill="none" stroke="var(--ink)" stroke-width="5"/>
      <line x1="212" y1="95" x2="190" y2="215" stroke="var(--rule)" stroke-width="1"/>
    </svg>
    <p class="wordmark">Marble Crest</p>
  </section>

</main>
</body>
</html>
```